RQT Livestock needs Buisness Card design using new logo

We need a business card design that ties our website and our new logo together. www.rqtlivestock-example.com The logo will be added to our website at a later date and replace the existing rqt livestock that is on the webpage. We are looking for a simple & professional design.

Target Market(s)

Cattle Producers, Ranchers

Industry/Entity Type

Agriculture

Contact Information for Business Card

Side one:
logo
www.rqtlivestock-example.com

Side two:
RQT Livestock
Robert & Tanya Quill
Fernhollow, MB Canada
(555) 318-2094/(555) 627-4185
quill47@fernwire-example.net

Font styles to use
Serif
Sans Serif
Script

Requirements
Must have
• We would like to tie our new logo in with our website on the business card.

```html
<!DOCTYPE html>
<html lang="en">
<head>
<meta charset="utf-8">
<title>RQT Livestock – Business Card</title>
<link rel="stylesheet" href="https://fonts.googleapis.com/css2?family=Source+Sans+3:ital,wght@0,400;0,600;1,400&display=swap">
<style>
  :root {
    --backdrop: #5e605f;
    --card-dark: #000000;
    --card-light: #ffffff;
    --ink-light: #ffffff;
    --ink-dark: #3a3a3c;
    --ink-text: #1d1d1f;
    --accent: #e0262a;
    --text-font: "Source Sans 3", "Myriad Pro", Arial, sans-serif;
  }
  * { box-sizing: border-box; margin: 0; padding: 0; }
  html, body {
    width: 1094px; height: 1200px; overflow: hidden;
    background: var(--backdrop);
    font-family: var(--text-font);
  }
  .card { position: absolute; left: 138px; width: 810px; height: 462px; }
  .card--front { top: 83px; background: var(--card-dark); }
  .card--back { top: 628px; background: var(--card-light); }

  .wordmark { position: absolute; font-weight: 400; line-height: 1; }
  .wordmark span { position: absolute; left: 0; right: 0; text-align: center; white-space: nowrap; }
  .wm-initials { letter-spacing: 0.04em; }

  .card--front .wordmark { left: 0; right: 0; top: 0; color: var(--ink-light); }
  .card--front .wm-initials { top: 80px; font-size: 132px; }
  .card--front .wm-word { top: 256px; font-size: 84px; }

  .front-url {
    position: absolute; left: 0; right: 0; top: 399px;
    text-align: center; color: var(--accent);
    font-size: 17px; line-height: 1; letter-spacing: 0.32em;
  }

  .card--back .wordmark { left: 70px; top: 0; width: 214px; color: var(--ink-dark); }
  .card--back .wm-initials { top: 70px; font-size: 76px; }
  .card--back .wm-word { top: 168px; font-size: 55px; }

  .identity { position: absolute; right: 75px; top: 0; text-align: right; color: var(--ink-text); line-height: 1; }
  .identity p { position: absolute; right: 0; white-space: nowrap; }
  .identity .company { top: 187px; font-size: 31px; font-weight: 600; letter-spacing: 0.12em; }
  .identity .owners { top: 227px; font-size: 38px; }

  .divider { position: absolute; left: 71px; top: 276px; width: 666px; height: 1px; background: var(--accent); }
  .location {
    position: absolute; right: 75px; top: 291px; line-height: 1;
    font-size: 18px; font-style: italic; color: var(--ink-text);
  }

  .contacts { position: absolute; top: 0; left: 0; right: 0; list-style: none; }
  .contact {
    position: absolute; display: flex; align-items: center; gap: 14px; line-height: 1;
    font-size: 17px; letter-spacing: 0.06em; color: var(--ink-text); white-space: nowrap;
  }
  .contact svg { width: 20px; height: 20px; fill: var(--accent); flex: none; }
  .contact--phone  { left: 226px; top: 346px; }
  .contact--mobile { left: 226px; top: 380px; }
  .contact--email  { left: 470px; top: 346px; letter-spacing: 0.01em; }
  .contact--web    { left: 470px; top: 380px; letter-spacing: 0.01em; }
</style>
</head>
<body>

<section class="card card--front" aria-label="Business card front">
  <div class="wordmark"><span class="wm-initials">RQT</span><span class="wm-word">Livestock</span></div>
  <p class="front-url">www.rqtlivestock-example.com</p>
</section>

<section class="card card--back" aria-label="Business card back">
  <div class="wordmark"><span class="wm-initials">RQT</span><span class="wm-word">Livestock</span></div>

  <div class="identity">
    <p class="company">RQT Livestock</p>
    <p class="owners">Robert &amp; Tanya Quill</p>
  </div>
  <div class="divider"></div>
  <p class="location">Fernhollow, MB Canada</p>

  <ul class="contacts">
    <li class="contact contact--phone">
      <svg viewBox="0 0 24 24" aria-hidden="true"><path d="M2 9c0-3 4-5 10-5s10 2 10 5v2h-5V9c-1-1-3-1-5-1s-4 0-5 1v2H2z"/><path d="M6 12h12l2 8H4z"/></svg>
      <span>(555) 627-4185</span>
    </li>
    <li class="contact contact--mobile">
      <svg viewBox="0 0 24 24" aria-hidden="true"><path d="M8 2h8a2 2 0 0 1 2 2v16a2 2 0 0 1-2 2H8a2 2 0 0 1-2-2V4a2 2 0 0 1 2-2zm1 4v6h6V6zm3 11a1.5 1.5 0 1 0 0 3 1.5 1.5 0 0 0 0-3z"/></svg>
      <span>(555) 318-2094</span>
    </li>
    <li class="contact contact--email">
      <svg viewBox="0 0 24 24" aria-hidden="true"><path d="M2 5h20v14H2zm2 2v.5l8 6 8-6V7zm0 3v7h16v-7l-8 6z"/></svg>
      <span>quill47@fernwire-example.net</span>
    </li>
    <li class="contact contact--web">
      <svg viewBox="0 0 24 24" aria-hidden="true"><path d="M12 2a10 10 0 1 0 0 20 10 10 0 0 0 0-20zm0 2c1 1 2 3 2.3 5H9.7C10 7 11 5 12 4zM4.3 11h3.4c0 1 .1 2 .3 3H4.6a8 8 0 0 1-.3-3zm.3-2A8 8 0 0 1 9 4.6 12 12 0 0 0 7.7 9zm5.1 2h4.6c0 1-.1 2-.3 3H10a13 13 0 0 1-.3-3zm6.6-2A12 12 0 0 0 15 4.6 8 8 0 0 1 19.4 9zm.3 2h3.4a8 8 0 0 1-.3 3h-3.4c.2-1 .3-2 .3-3z"/></svg>
      <span>www.rqtlivestock-example.com</span>
    </li>
  </ul>
</section>

</body>
</html>
```